stationary deign for trucking company

im a trucking company looking for a professional set of stationary designs i deliver goods from point a to b
Updates

When submitting stationary designs I need envelope design, letterhead, cards, I’d badge etc

Industry/Entity Type

Trucking Company

Requirements
Must have
• must have letter head, business card, envelope, fax sheet, id badge, folder, thank you card, notebook, invoice sheet.
Nice to have
• nice to have them all custom made (letterhead,envelope, business card, I’d badge etc
Should not have
• must not have prepaid sign want i unique design for items

```html
<!DOCTYPE html>
<html lang="en">
<head>
<meta charset="utf-8">
<title>Harlow Freight + Logistics — Presentation Folder</title>
<link href="https://fonts.googleapis.com/css2?family=Lato:wght@400;700&display=swap" rel="stylesheet">
<style>
  :root {
    --stage: #2a2a2a;
    --brand-blue: #0c57a5;
    --spine: #050607;
    --paper: #ffffff;
    --paper-soft: #f7f8fa;
    --paper-fold: #ececee;
    --ink: #111111;
  }
  * { margin: 0; padding: 0; box-sizing: border-box; }
  html, body { width: 915px; height: 1200px; overflow: hidden; background: var(--stage); }
  body { position: relative; font-family: "Lato", Arial, sans-serif; }

  .folder-inside {
    position: absolute; left: 31px; top: 20px; width: 853px; height: 568px;
  }
  .folder-inside svg { display: block; }

  .folder-outside {
    position: absolute; left: 31px; top: 608px; width: 854px; height: 569px;
  }
  .back-cover {
    position: absolute; left: 0; top: 0; width: 427px; height: 569px;
    background: var(--brand-blue); color: var(--paper);
  }
  .spine {
    position: absolute; left: 427px; top: 0; width: 48px; height: 569px;
    background: var(--spine);
  }
  .front-cover {
    position: absolute; left: 475px; top: 0; width: 379px; height: 569px;
    background: linear-gradient(90deg, var(--paper-soft), var(--paper));
  }

  .brand-name {
    font-family: "Lato", Arial, sans-serif; font-weight: 700;
    text-transform: uppercase; line-height: 1;
  }
  .brand-name .line { display: block; }
  .back-cover .brand-name {
    position: absolute; left: 40px; top: 52px; color: var(--paper);
  }
  .back-cover .brand-name .main { font-size: 36px; letter-spacing: 5px; }
  .back-cover .brand-name .sub { font-size: 10.5px; letter-spacing: 3.4px; margin-top: 7px; }

  .front-cover .brand-name {
    position: absolute; left: 0; right: 0; top: 58px; text-align: center; color: var(--ink);
  }
  .front-cover .brand-name .main { font-size: 27px; letter-spacing: 4px; }
  .front-cover .brand-name .sub { font-size: 8px; letter-spacing: 2.6px; margin-top: 5px; }

  .contact {
    position: absolute; top: 802px; font-size: 9px; line-height: 14px; color: var(--paper);
  }
  .contact-list { position: absolute; top: 518px; list-style: none; font-size: 9px; line-height: 14px; }
  .contact-list li { display: flex; align-items: center; gap: 6px; white-space: nowrap; }
  .contact-list svg { width: 7px; height: 7px; flex: none; }
  .contact-phone { left: 23px; }
  .contact-web { left: 153px; }
  .contact-address { left: 311px; line-height: 16px; top: 516px; }

  .front-website {
    position: absolute; left: 0; right: 0; top: 527px; text-align: center;
    font-size: 9.5px; color: var(--ink); letter-spacing: 0.3px;
  }
  .front-website::after {
    content: ""; display: block; width: 36px; height: 1px; margin: 6px auto 0;
    background: var(--brand-blue);
  }
</style>
</head>
<body>

  <section class="folder-inside" aria-label="Folder inside spread">
    <svg width="853" height="568" viewBox="0 0 853 568">
      <defs>
        <linearGradient id="leftPanel" x1="0" x2="1" y1="0" y2="0">
          <stop offset="0" stop-color="#ffffff"/>
          <stop offset="1" stop-color="#ececee"/>
        </linearGradient>
        <linearGradient id="rightPanel" x1="0" x2="1" y1="0" y2="0">
          <stop offset="0" stop-color="#f6f7f9"/>
          <stop offset="1" stop-color="#ffffff"/>
        </linearGradient>
      </defs>
      <rect class="inside-left" x="0" y="0" width="427" height="568" fill="url(#leftPanel)"/>
      <rect class="inside-right" x="427" y="0" width="426" height="568" fill="url(#rightPanel)"/>
      <polygon class="pocket-left" points="0,378 403,378 423,568 0,568" fill="#0c57a5"/>
      <polygon class="pocket-right" points="450,378 853,378 853,568 430,568" fill="#0c57a5"/>
      <g class="card-slits" stroke="#ffffff" stroke-width="0.8">
        <line x1="127" y1="446" x2="150" y2="422"/>
        <line x1="276" y1="422" x2="298" y2="446"/>
        <line x1="127" y1="500" x2="150" y2="523"/>
        <line x1="276" y1="523" x2="298" y2="500"/>
        <line x1="555" y1="446" x2="578" y2="422"/>
        <line x1="704" y1="422" x2="727" y2="446"/>
        <line x1="555" y1="500" x2="578" y2="523"/>
        <line x1="704" y1="523" x2="727" y2="500"/>
      </g>
    </svg>
  </section>

  <section class="folder-outside" aria-label="Folder outside spread">
    <div class="back-cover">
      <h2 class="brand-name">
        <span class="line main">Harlow</span>
        <span class="line sub">Freight + Logistics</span>
      </h2>

      <ul class="contact-list contact-phone">
        <li>
          <svg viewBox="0 0 10 10"><path d="M2 0.5 L4 2.5 L3 4 Q4.5 6 6 7 L7.5 6 L9.5 8 L8 9.5 Q3 9 0.5 2 Z" fill="#fff"/></svg>
          555-014-2620
        </li>
        <li>
          <svg viewBox="0 0 10 10"><rect x="2.5" y="0.5" width="5" height="9" rx="1" fill="none" stroke="#fff" stroke-width="1.2"/></svg>
          555-014-2620
        </li>
      </ul>

      <ul class="contact-list contact-web">
        <li>
          <svg viewBox="0 0 10 10"><rect x="0.5" y="2" width="9" height="6" fill="#fff"/><path d="M0.5 2 L5 5.5 L9.5 2" fill="none" stroke="#0c57a5" stroke-width="0.8"/></svg>
          info@harlowfreight.com
        </li>
        <li>
          <svg viewBox="0 0 10 10"><circle cx="5" cy="5" r="4.3" fill="none" stroke="#fff" stroke-width="1"/><path d="M0.7 5 H9.3 M5 0.7 Q2 5 5 9.3 M5 0.7 Q8 5 5 9.3" fill="none" stroke="#fff" stroke-width="0.8"/></svg>
          www.harlowfreight.com
        </li>
      </ul>

      <address class="contact-list contact-address" style="font-style: normal;">
        4820 Mercer Ridge Rd.<br>
        Suite 210, TX 70000
      </address>
    </div>

    <div class="spine"></div>

    <div class="front-cover">
      <h1 class="brand-name">
        <span class="line main">Harlow</span>
        <span class="line sub">Freight + Logistics</span>
      </h1>
      <p class="front-website">www.harlowfreight.com</p>
    </div>
  </section>

</body>
</html>
```